Financial investment & advisory business needs a powerpoint design

We need a powerpoint design incorporating the logo (and colours) and relating to the business card design we already have. The company is a boutique financial investment and advisory business called Brevora Holdings Pty Ltd based in Australia. The final design should communicate innovative advice and financial safety and growth. A young, contemporary but experienced, professional business.

Target Market(s)

Companies listed or wishing to list on the Tarrowin Stock Exchange and Professional and Institutional Investors.

Industry/Entity Type

Finance

Requirements
Must have
• Incorporate the logo and colours. Be similar/relate to the business card design.
Nice to have
Should not have
• Do not deviate from the logo colours.
• Do not use black background or invert the logo.
• Do not deviate from the business card design too much.

```html
<!DOCTYPE html>
<html lang="en">
<head>
<meta charset="utf-8">
<title>Brevora Holdings – Company Presentation Deck</title>
<link href="https://fonts.googleapis.com/css2?family=Carlito:wght@400;700&display=swap" rel="stylesheet">
<style>
:root{
  --blue:#3f6db3;
  --blue-dark:#2c4f8e;
  --blue-light:#6f98d4;
  --blue-pale:#d9e3f2;
  --grey:#8a8a8a;
  --grey-dark:#5e5e5e;
  --grey-light:#c9c9c9;
  --ink:#4a4a4a;
  --paper:#ffffff;
  --frame:#b9b9b9;
  --night-top:#1b2850;
  --night-mid:#35508f;
  --night-low:#0c1430;
}
*{box-sizing:border-box;margin:0;padding:0}
html,body{width:1200px;height:408px;overflow:hidden;background:#fff}
body{font-family:"Carlito",Calibri,Arial,sans-serif;color:var(--ink);position:relative}
.slide{position:absolute;width:237px;height:131px;background:var(--paper);border:1px solid var(--frame);overflow:hidden}
.abs{position:absolute}
.accent{position:absolute;left:10px;top:7px;width:18px;height:1.5px;background:var(--blue)}
.title{position:absolute;left:10px;top:10px;font-size:8px;font-weight:700;color:var(--blue);line-height:1}
.title b{font-weight:700}
.title span{font-weight:400}
.sub{position:absolute;left:10px;top:19px;font-size:3.6px;color:var(--grey)}
.p{font-size:2.6px;line-height:1.35;color:var(--grey)}
.label{font-size:2.8px;font-weight:700;color:var(--blue)}
.footer{position:absolute;left:0;right:0;bottom:0;height:10px;background:var(--paper)}
.brand{position:absolute;left:6px;top:0;line-height:10px;font-size:5px;font-weight:700;color:var(--blue-dark);letter-spacing:.3px}
.band{position:absolute;left:95px;top:2px}
.copy{position:absolute;left:135px;top:2px;line-height:8px;font-size:3px;font-weight:700;color:#fff}
.page{position:absolute;right:0;top:2px;width:12px;height:8px;background:var(--blue-light);color:#fff;font-size:3px;text-align:center;line-height:8px}
.photo-night{background:linear-gradient(180deg,var(--night-top) 0%,var(--night-mid) 55%,#6b6a8f 72%,var(--night-low) 100%)}
.photo-sky{background:linear-gradient(160deg,#5a86c9 0%,#a9c3e6 45%,#e9eef6 70%,#7a9bd0 100%)}
.icon-circle{position:absolute;border-radius:50%;background:var(--blue)}
.table{position:absolute;left:10px;top:30px;width:210px;border-collapse:collapse;font-size:3px}
.table th{background:var(--blue-dark);color:#fff;height:8px;font-weight:700;border:.5px solid #fff}
.table td{height:9px;border:.5px solid #fff;background:var(--blue-pale);color:var(--grey-dark);text-align:center}
.table tr:nth-child(even) td{background:#edf1f8}
.table td:first-child{background:#b7c7e3}
.contact-row{display:flex;align-items:center;gap:3px;font-size:3.6px;color:var(--grey-dark);margin-bottom:4px}
.dot{width:6px;height:6px;border-radius:50%;background:var(--blue);flex:none}
.big-white{color:#fff;font-weight:700}
</style>
</head>
<body>

<!-- Row 1 -->
<section class="slide" style="left:0;top:0">
  <div class="abs photo-night" style="inset:0" role="img" aria-label="Night skyline of a city with lit towers reflected in water"></div>
  <svg class="abs" style="inset:0" width="237" height="131" viewBox="0 0 237 131">
    <defs><linearGradient id="coverBlue" x1="0" y1="0" x2="1" y2="1"><stop offset="0" stop-color="#3f6db3" stop-opacity=".85"/><stop offset="1" stop-color="#2c4f8e" stop-opacity=".95"/></linearGradient></defs>
    <polygon points="0,0 95,0 0,55" fill="#ffffff" opacity=".85"/>
    <polygon points="237,0 237,131 95,131" fill="url(#coverBlue)"/>
  </svg>
  <div class="brand" style="top:6px;font-size:7px;color:var(--blue-dark)">Brevora Holdings</div>
  <div class="abs big-white" style="right:10px;bottom:10px;font-size:11px;line-height:1.15;text-align:right">Company<br>Presentation</div>
</section>

<section class="slide" style="left:241px;top:0">
  <div class="accent"></div>
  <div class="title">Brevora <span>At Glance</span></div>
  <div class="sub" style="width:120px;line-height:1.3">Brief team story and values of our firm with a short note here</div>
  <div class="abs photo-sky" style="left:140px;top:0;width:97px;height:121px" role="img" aria-label="Clear bubble floating against a blue sky with clouds"></div>
  <p class="abs p" style="left:10px;top:35px;width:118px">Our advisers guide listed firms through growth with clear steady counsel and care for capital.</p>
  <div class="abs" style="left:10px;top:52px;width:118px;height:17px;background:var(--grey);padding:2px 3px"><p class="p" style="color:#fff;font-weight:700">We pair fresh thinking with long market experience to keep capital safe and growing.</p></div>
  <p class="abs p" style="left:10px;top:73px;width:118px">Each mandate is built on trust, discipline and careful review of every risk.</p>
  <footer class="footer"><div class="brand">Brevora Holdings</div><svg class="band" width="142" height="8"><polygon points="0,8 8,0 142,0 142,8" fill="var(--blue)"/></svg><div class="copy">© Brevora Holdings 2017</div><div class="page">2</div></footer>
</section>

<section class="slide" style="left:482px;top:0">
  <div class="accent"></div>
  <div class="title">Team/Company <span>Principles</span></div>
  <div class="sub">Short team principles description</div>
  <svg class="abs" style="inset:0" width="237" height="131" viewBox="0 0 237 131">
    <g stroke="#c9c9c9" stroke-width=".6">
      <line x1="95" y1="47" x2="118" y2="66"/><line x1="95" y1="59" x2="118" y2="66"/><line x1="95" y1="73" x2="118" y2="66"/><line x1="95" y1="95" x2="118" y2="66"/>
      <line x1="141" y1="47" x2="118" y2="66"/><line x1="141" y1="59" x2="118" y2="66"/><line x1="141" y1="73" x2="118" y2="66"/><line x1="141" y1="95" x2="118" y2="66"/>
    </g>
    <circle cx="118" cy="66" r="17" fill="#3f6db3"/>
    <g fill="#ffffff"><circle cx="118" cy="60" r="2.5"/><rect x="115" y="63" width="6" height="9" rx="1.5"/><circle cx="111" cy="62" r="2"/><rect x="109" y="64.5" width="4.5" height="7" rx="1.2"/><circle cx="125" cy="62" r="2"/><rect x="122.5" y="64.5" width="4.5" height="7" rx="1.2"/></g>
    <g fill="#8a8a8a"><circle cx="95" cy="47" r="4"/><circle cx="95" cy="59" r="4"/><circle cx="95" cy="73" r="4"/><circle cx="95" cy="95" r="4"/><circle cx="141" cy="47" r="4"/><circle cx="141" cy="59" r="4"/><circle cx="141" cy="73" r="4"/><circle cx="141" cy="95" r="4"/></g>
    <g fill="#fff" font-size="3" font-weight="700" text-anchor="middle" font-family="Carlito, sans-serif"><text x="95" y="48">01</text><text x="95" y="60">03</text><text x="95" y="74">05</text><text x="95" y="96">07</text><text x="141" y="48">02</text><text x="141" y="60">04</text><text x="141" y="74">06</text><text x="141" y="96">08</text></g>
    <g font-family="Carlito, sans-serif"><g font-size="2.6" font-weight="700" fill="#3f6db3" text-anchor="end"><text x="86" y="45">LOREM OPTION</text><text x="86" y="57">LOREM OPTION</text><text x="86" y="71">LOREM OPTION</text><text x="86" y="93">LOREM OPTION</text></g>
    <g font-size="2.2" fill="#8a8a8a" text-anchor="end"><text x="86" y="48.5">Short note on this principle here</text><text x="86" y="60.5">Short note on this principle here</text><text x="86" y="74.5">Short note on this principle here</text><text x="86" y="96.5">Short note on this principle here</text></g>
    <g font-size="2.6" font-weight="700" fill="#3f6db3"><text x="150" y="45">LOREM OPTION</text><text x="150" y="57">LOREM OPTION</text><text x="150" y="71">LOREM OPTION</text><text x="150" y="93">LOREM OPTION</text></g>
    <g font-size="2.2" fill="#8a8a8a"><text x="150" y="48.5">Short note on this principle here</text><text x="150" y="60.5">Short note on this principle here</text><text x="150" y="74.5">Short note on this principle here</text><text x="150" y="96.5">Short note on this principle here</text></g></g>
  </svg>
  <footer class="footer"><div class="brand">Brevora Holdings</div><svg class="band" width="142" height="8"><polygon points="0,8 8,0 142,0 142,8" fill="var(--blue)"/></svg><div class="copy">© Brevora Holdings 2017</div><div class="page">3</div></footer>
</section>

<section class="slide" style="left:723px;top:0">
  <div class="accent"></div>
  <div class="title">Company <span>History</span></div>
  <div class="sub">Short time line description</div>
  <svg class="abs" style="inset:0" width="237" height="131" viewBox="0 0 237 131" font-family="Carlito, sans-serif">
    <rect x="15" y="76" width="212" height="4" rx="2" fill="#3f6db3"/>
    <g fill="#fff" stroke="#3f6db3" stroke-width="1.2"><circle cx="38" cy="78" r="4.5"/><circle cx="83" cy="78" r="4.5"/><circle cx="128" cy="78" r="4.5"/><circle cx="173" cy="78" r="4.5"/><circle cx="218" cy="78" r="4.5"/></g>
    <g fill="#3f6db3"><circle cx="38" cy="78" r="1.6"/><circle cx="83" cy="78" r="1.6"/><circle cx="128" cy="78" r="1.6"/><circle cx="173" cy="78" r="1.6"/><circle cx="218" cy="78" r="1.6"/></g>
    <g font-size="2.8" fill="#5e5e5e" text-anchor="middle" font-weight="700"><text x="38" y="88">2007</text><text x="83" y="72">2012</text><text x="128" y="88">2013</text><text x="173" y="72">2015</text><text x="218" y="88">2019</text></g>
    <g font-size="2.8" fill="#3f6db3" font-weight="700" text-anchor="middle"><text x="45" y="44">STUDIO INSIGHT</text><text x="128" y="44">IT EXPANSION</text><text x="200" y="44">TOP BRANCH LIST</text><text x="83" y="96">INVESTMENT</text><text x="173" y="96">NATIONAL EXPANSION</text></g>
    <g font-size="2.2" fill="#8a8a8a" text-anchor="middle"><text x="45" y="48">Short note on this year here</text><text x="128" y="48">Short note on this year here</text><text x="200" y="48">Short note on this year here</text><text x="83" y="100">Short note on this year here</text><text x="173" y="100">Short note on this year here</text></g>
    <g stroke="#c9c9c9" stroke-width=".5"><line x1="128" y1="52" x2="128" y2="73"/><line x1="200" y1="52" x2="218" y2="73"/><line x1="45" y1="52" x2="38" y2="73"/></g>
  </svg>
  <footer class="footer"><div class="brand">Brevora Holdings</div><svg class="band" width="142" height="8"><polygon points="0,8 8,0 142,0 142,8" fill="var(--blue)"/></svg><div class="copy">© Brevora Holdings 2017</div><div class="page">4</div></footer>
</section>

<section class="slide" style="left:963px;top:0">
  <div class="accent"></div>
  <div class="title">Project/Client <span>Showcase</span></div>
  <div class="sub">Short project description</div>
  <div class="abs" style="left:10px;top:28px;width:200px;height:24px;background:var(--grey);padding:3px 4px">
    <div style="font-size:3.2px;font-weight:700;color:#fff">CLIENT LOREM COMPANY</div>
    <p class="p" style="color:#fff;width:95px;margin-top:1px">Short note on the client and the work we did for them</p>
  </div>
  <div class="abs" style="left:126px;top:34px;width:80px;height:58px;background:linear-gradient(180deg,#3a3a3a,#1e1e1e);border-radius:2px" role="img" aria-label="Laptop showing the client project"></div>
  <div class="abs" style="left:12px;top:58px;width:100px">
    <div class="contact-row" style="font-size:2.4px;margin-bottom:3px"><span class="dot" style="width:4px;height:4px"></span>Brief point about the project result here</div>
    <div class="contact-row" style="font-size:2.4px"><span class="dot" style="width:4px;height:4px"></span>Brief point about the project result here</div>
  </div>
  <p class="abs p" style="left:10px;top:102px;width:110px">A closing line on outcomes for this client</p>
  <footer class="footer"><div class="brand">Brevora Holdings</div><svg class="band" width="142" height="8"><polygon points="0,8 8,0 142,0 142,8" fill="var(--blue)"/></svg><div class="copy">© Brevora Holdings 2017</div><div class="page">5</div></footer>
</section>

<!-- Row 2 -->
<section class="slide" style="left:0;top:137px">
  <div class="accent"></div>
  <div class="title">Services <span>Show</span></div>
  <div class="sub">Short services description</div>
  <svg class="abs" style="inset:0" width="237" height="131" viewBox="0 0 237 131" font-family="Carlito, sans-serif">
    <g fill="#3f6db3"><circle cx="38" cy="60" r="10"/><circle cx="90" cy="60" r="10"/><circle cx="142" cy="60" r="10"/><circle cx="194" cy="60" r="10"/></g>
    <g fill="none" stroke="#fff" stroke-width="1"><rect x="33" y="56" width="10" height="7"/><line x1="38" y1="63" x2="38" y2="65.5"/><line x1="35" y1="65.5" x2="41" y2="65.5"/>
      <rect x="87" y="54" width="6" height="12" rx="1"/>
      <line x1="137" y1="65" x2="146" y2="56"/>
      <rect x="189" y="55" width="8" height="6" rx="1"/><rect x="192" y="59" width="7" height="5" rx="1"/></g>
    <g font-size="2.8" font-weight="700" fill="#3f6db3" text-anchor="middle"><text x="38" y="78">DESIGN &amp; UX</text><text x="90" y="78">MOBILE APPS</text><text x="142" y="78">COPYWRITING</text><text x="194" y="78">SOCIAL MARKETING</text></g>
    <g font-size="2.3" fill="#8a8a8a" text-anchor="middle"><text x="38" y="83">Short line on what this</text><text x="38" y="86">service covers</text><text x="90" y="83">Short line on what this</text><text x="90" y="86">service covers</text><text x="142" y="83">Short line on what this</text><text x="142" y="86">service covers</text><text x="194" y="83">Short line on what this</text><text x="194" y="86">service covers</text></g>
  </svg>
  <footer class="footer"><div class="brand">Brevora Holdings</div><svg class="band" width="142" height="8"><polygon points="0,8 8,0 142,0 142,8" fill="var(--blue)"/></svg><div class="copy">© Brevora Holdings 2017</div><div class="page">6</div></footer>
</section>

<section class="slide" style="left:241px;top:137px">
  <div class="accent"></div>
  <div class="title">Annual <span>Revenue</span></div>
  <div class="sub">Short financial results review</div>
  <div class="abs label" style="left:10px;top:47px">LOREM IPSUM TITLE</div>
  <p class="abs p" style="left:10px;top:51px;width:75px">Revenue grew across most years with a strong peak in the middle year and steady gains after it.</p>
  <svg class="abs" style="inset:0" width="237" height="131" viewBox="0 0 237 131" font-family="Carlito, sans-serif">
    <g opacity=".85"><polygon points="92,110 112,60 132,110" fill="#8a8a8a"/><polygon points="112,110 132,70 152,110" fill="#8a8a8a"/><polygon points="152,110 172,62 192,110" fill="#8a8a8a"/><polygon points="172,110 192,54 212,110" fill="#8a8a8a"/></g>
    <polygon points="132,110 152,44 172,110" fill="#3f6db3"/>
    <rect x="92" y="109" width="120" height="3" rx="1.5" fill="#2c4f8e"/>
    <g font-size="2.8" fill="#8a8a8a" text-anchor="middle"><text x="112" y="57">15.25%</text><text x="132" y="67">13.10%</text><text x="172" y="59">15.3%</text><text x="192" y="51">17.12%</text></g>
    <text x="152" y="41" font-size="3.2" font-weight="700" fill="#3f6db3" text-anchor="middle">18.2%</text>
    <g font-size="2.2" fill="#fff" text-anchor="middle"><text x="112" y="111.3">2010</text><text x="132" y="111.3">2011</text><text x="152" y="111.3">2012</text><text x="172" y="111.3">2013</text><text x="192" y="111.3">2014</text></g>
  </svg>
  <footer class="footer"><div class="brand">Brevora Holdings</div><svg class="band" width="142" height="8"><polygon points="0,8 8,0 142,0 142,8" fill="var(--blue)"/></svg><div class="copy">© Brevora Holdings 2017</div><div class="page">7</div></footer>
</section>

<section class="slide" style="left:482px;top:137px">
  <div class="abs photo-night" style="inset:0" role="img" aria-label="Night skyline of a city with lit towers reflected in water"></div>
  <svg class="abs" style="inset:0" width="237" height="131" viewBox="0 0 237 131">
    <polygon points="0,0 60,0 0,131" fill="#ffffff" opacity=".75"/>
    <polygon points="237,0 237,131 150,131" fill="#3f6db3" opacity=".9"/>
  </svg>
  <div class="brand" style="top:6px;font-size:7px;color:var(--blue-dark)">Brevora Holdings</div>
  <div class="abs big-white" style="right:8px;bottom:8px;font-size:10px">Section Slide</div>
</section>

<section class="slide" style="left:723px;top:137px">
  <div class="accent"></div>
  <div class="title">Global <span>Presence</span></div>
  <div class="sub">Short description for the global presence</div>
  <div class="abs" style="left:62px;top:34px;width:120px;height:62px;background:linear-gradient(180deg,#9a9a9a,#7d7d7d);border-radius:6px" role="img" aria-label="World map with office locations"></div>
  <svg class="abs" style="inset:0" width="237" height="131" viewBox="0 0 237 131" font-family="Carlito, sans-serif">
    <g fill="#3f6db3"><circle cx="42" cy="48" r="13"/><circle cx="42" cy="94" r="12"/><circle cx="96" cy="92" r="11"/><circle cx="155" cy="92" r="10"/><circle cx="205" cy="52" r="11"/><circle cx="208" cy="94" r="10"/></g>
    <g font-size="2.6" font-weight="700" fill="#fff" text-anchor="middle"><text x="42" y="46">AL ARABIA</text><text x="42" y="92">AMERICA</text><text x="96" y="90">EUROPE</text><text x="155" y="90">AFRICA</text><text x="205" y="50">ASIA</text><text x="208" y="92">AUSTRALIA</text></g>
    <g font-size="2.2" fill="#fff" text-anchor="middle"><text x="42" y="50">Short office note</text><text x="42" y="96">Short office note</text><text x="96" y="94">Short office note</text><text x="155" y="94">Short office note</text><text x="205" y="54">Short office note</text><text x="208" y="96">Short office note</text></g>
  </svg>
  <footer class="footer"><div class="brand">Brevora Holdings</div><svg class="band" width="142" height="8"><polygon points="0,8 8,0 142,0 142,8" fill="var(--blue)"/></svg><div class="copy">© Brevora Holdings 2017</div><div class="page">9</div></footer>
</section>

<section class="slide" style="left:963px;top:137px">
  <div class="accent"></div>
  <div class="title">Infographic <span>Puzzle</span></div>
  <div class="sub">Short description</div>
  <div class="abs" style="left:108px;top:38px;width:42px;height:42px;transform:rotate(45deg);background:linear-gradient(135deg,#3f6db3 0 50%,#8a8a8a 50% 100%)" role="img" aria-label="Puzzle pieces joined into a diamond"></div>
  <svg class="abs" style="inset:0" width="237" height="131" viewBox="0 0 237 131" font-family="Carlito, sans-serif">
    <g stroke="#c9c9c9" stroke-width=".5"><line x1="140" y1="40" x2="170" y2="40"/><line x1="150" y1="58" x2="175" y2="58"/><line x1="108" y1="70" x2="85" y2="70"/><line x1="140" y1="85" x2="175" y2="85"/></g>
    <g font-size="2.8" font-weight="700" fill="#3f6db3"><text x="174" y="40">MARKETING</text><text x="178" y="57">SEO ACHIEVEMENTS</text><text x="180" y="84">TOP LIST LAYOUT</text><text x="82" y="68" text-anchor="end">SEARCH &amp; RESULTS</text></g>
    <g font-size="2.2" fill="#8a8a8a"><text x="174" y="44">Short line on this part of the plan</text><text x="178" y="61">Short line on this part of the plan</text><text x="180" y="88">Short line on this part of the plan</text><text x="82" y="72" text-anchor="end">Short line on this part of the plan</text></g>
  </svg>
  <footer class="footer"><div class="brand">Brevora Holdings</div><svg class="band" width="142" height="8"><polygon points="0,8 8,0 142,0 142,8" fill="var(--blue)"/></svg><div class="copy">© Brevora Holdings 2017</div><div class="page">10</div></footer>
</section>

<!-- Row 3 -->
<section class="slide" style="left:0;top:273px">
  <div class="accent"></div>
  <div class="title">Services <span>Process</span></div>
  <div class="sub">Short description</div>
  <svg class="abs" style="inset:0" width="237" height="131" viewBox="0 0 237 131" font-family="Carlito, sans-serif">
    <g fill="none" stroke-width="8">
      <path d="M20,82 A22,22 0 0 1 64,82" stroke="#8a8a8a"/>
      <path d="M64,82 A22,22 0 0 0 108,82" stroke="#3f6db3"/>
      <path d="M108,82 A22,22 0 0 1 152,82" stroke="#8a8a8a"/>
      <path d="M152,82 A22,22 0 0 0 196,82" stroke="#a6a6a6"/>
      <path d="M196,82 A22,22 0 0 1 224,68" stroke="#c9c9c9"/>
    </g>
    <g fill="#3f6db3"><circle cx="42" cy="82" r="3"/><circle cx="86" cy="82" r="3"/><circle cx="130" cy="82" r="3"/><circle cx="174" cy="82" r="3"/><circle cx="212" cy="82" r="3"/></g>
    <g font-size="2.4" font-weight="700" fill="#fff" text-anchor="middle"><text x="42" y="61">CREATIVE IDEA</text><text x="86" y="104">RESEARCH</text><text x="130" y="61">STRATEGY</text><text x="174" y="104">DESIGN</text><text x="212" y="67">LAUNCH</text></g>
    <g font-size="2.2" fill="#8a8a8a" text-anchor="middle"><text x="42" y="108">Short step note here</text><text x="86" y="50">Short step note here</text><text x="130" y="108">Short step note here</text><text x="174" y="50">Short step note here</text><text x="212" y="108">Short step note here</text></g>
  </svg>
  <footer class="footer"><div class="brand">Brevora Holdings</div><svg class="band" width="142" height="8"><polygon points="0,8 8,0 142,0 142,8" fill="var(--blue)"/></svg><div class="copy">© Brevora Holdings 2017</div><div class="page">11</div></footer>
</section>

<section class="slide" style="left:241px;top:273px">
  <div class="accent"></div>
  <div class="title">Disclaimer</div>
  <p class="abs p" style="left:10px;top:24px;width:200px;font-size:3px">This material is general information only and does not take into account your objectives, financial situation or needs. Consider whether it suits you before acting and seek advice where needed. Past results are not a reliable guide to future returns.</p>
  <footer class="footer"><div class="brand">Brevora Holdings</div><svg class="band" width="142" height="8"><polygon points="0,8 8,0 142,0 142,8" fill="var(--blue)"/></svg><div class="copy">© Brevora Holdings 2017</div><div class="page">12</div></footer>
</section>

<section class="slide" style="left:482px;top:273px">
  <div class="accent"></div>
  <div class="title">Table <span>Info</span></div>
  <div class="sub">Please insert the table info</div>
  <table class="table">
    <tr><th>Column 1</th><th>Column 2</th><th>Column 3</th><th>Column 4</th><th>Column 5</th><th>Column 6</th></tr>
    <tr><td>Row 1</td><td></td><td></td><td></td><td></td><td></td></tr>
    <tr><td>Row 2</td><td></td><td></td><td></td><td></td><td></td></tr>
    <tr><td>Row 3</td><td></td><td></td><td></td><td></td><td></td></tr>
    <tr><td>Row 4</td><td></td><td></td><td></td><td></td><td></td></tr>
    <tr><td>Row 5</td><td></td><td></td><td></td><td></td><td></td></tr>
    <tr><td>Row 6</td><td></td><td></td><td></td><td></td><td></td></tr>
    <tr><td>Row 7</td><td></td><td></td><td></td><td></td><td></td></tr>
  </table>
  <footer class="footer"><div class="brand">Brevora Holdings</div><svg class="band" width="142" height="8"><polygon points="0,8 8,0 142,0 142,8" fill="var(--blue)"/></svg><div class="copy">© Brevora Holdings 2017</div><div class="page">13</div></footer>
</section>

<section class="slide" style="left:723px;top:273px">
  <div class="accent"></div>
  <div class="title" style="color:var(--grey-dark);font-weight:400">Contact Information</div>
  <div class="sub">Please contact us through one of the communication channels below.</div>
  <div class="abs" style="left:30px;top:40px;width:90px">
    <div class="label" style="font-size:3.6px;margin-bottom:4px">Contact us</div>
    <div class="contact-row"><span class="dot"></span>42 Harwick Lane, Tarrowin City</div>
    <div class="contact-row"><span class="dot"></span>000 412 887 310</div>
    <div class="contact-row"><span class="dot"></span>hello@brevora-mail.com</div>
  </div>
  <div class="abs" style="left:138px;top:40px;width:90px">
    <div class="label" style="font-size:3.6px;margin-bottom:4px">Follow us on</div>
    <div class="contact-row"><span class="dot"></span>social/brevoraholdings</div>
    <div class="contact-row"><span class="dot"></span>@brevorahq</div>
    <div class="contact-row"><span class="dot"></span>team@brevora-mail.com</div>
  </div>
  <footer class="footer"><div class="brand">Brevora Holdings</div><svg class="band" width="142" height="8"><polygon points="0,8 8,0 142,0 142,8" fill="var(--blue)"/></svg><div class="copy">© Brevora Holdings 2017</div><div class="page">14</div></footer>
</section>

<section class="slide" style="left:963px;top:273px">
  <div class="abs photo-night" style="inset:0" role="img" aria-label="Night skyline of a city with lit towers reflected in water"></div>
  <svg class="abs" style="inset:0" width="237" height="131" viewBox="0 0 237 131">
    <polygon points="237,0 237,131 120,131" fill="#ffffff" opacity=".9"/>
  </svg>
  <div class="abs big-white" style="left:8px;top:94px;font-size:10px">Thank you for your time</div>
  <div class="brand" style="left:auto;right:8px;top:auto;bottom:4px;font-size:7px;color:var(--blue-dark)">Brevora Holdings</div>
</section>

</body>
</html>
```